Forget what you know about corporate well

I need a one-page flies used for print, to embedding in a website, all social media platforms and email.

Target Market(s)

Business

Industry/Entity Type

Health And Wellness

Font styles to use
Serif
Script
Other font styles liked:
• I would like the designers opinion on the font

Colors

Designer to choose colors to be used in the design.

Requirements
Must have
• This is the wording:
• Did you know that 75% of healthcare costs are incurred by preventable diseases? Cardiovascular disease, cancer, and diabetes are the three major causes of rising health care plans and are all preventable.
• Milo and his team have spent decades learning how to increase productivity, reduce absenteeism, and increase employee engagement, all leading to lowering healthcare costs. Together, they have developed a system created to target the masses all while addressing individual needs. Their corporate training challenges helps to engrain positive habits through a carefully curated accountability and reward system.
• How it works:
• Step 1 – evaluate the needs of your business;
• Step 2 – set up individualized workshops based on highest needs;
• Step 3 – create a customized corporate training challenge.
• Why Milo?
• Milo excels at motivational speaking. He is an author, a nutritionist and a professional athlete with a master’s degree in clinical nutrition. He is a teacher of corporate wellness at Fernhollow College and a health coach. Milo has been featured in national magazines, podcasts, and popular fitness websites. Milo’s own health issues put him on a quest to heal himself and others. With twenty-five years of experience and a passion for wellness, he can provide your company with an unforgettable experience.
Nice to have
• I will not give my opinion, I believe that is an insult to the designer. All of the verbiage is above and I attached a plethora of pictures.
Should not have
• No opinion

```html
<!DOCTYPE html>
<html lang="en">
<head>
<meta charset="utf-8">
<title>Milo – Corporate Wellness Flyer</title>
<link href="https://fonts.googleapis.com/css2?family=Lato:wght@400;700&display=swap" rel="stylesheet">
<style>
  :root{
    --backdrop:#e9ecee;
    --lime:#cfe84a;
    --olive-dark:#3a4810;
    --olive:#5b7013;
    --panel:#bdbdbd;
    --hex:#6d6d6d;
    --tab:#8a8a8a;
    --footer:#666666;
    --ink:#2b2b2b;
    --white:#ffffff;
  }
  html,body{margin:0;padding:0;width:1200px;height:1200px;overflow:hidden;background:var(--backdrop);}
  .flyer{
    position:absolute;left:158px;top:27px;width:842px;height:1090px;
    transform:scale(1.05);transform-origin:0 0;
    background:var(--white);overflow:hidden;
    font-family:'Lato',sans-serif;color:var(--ink);
    box-shadow:0 4px 18px rgba(0,0,0,.18);
  }
  .flyer-shapes{position:absolute;left:0;top:0;width:842px;height:1090px;}
  .abs{position:absolute;margin:0;}
  .hero-question{right:38px;top:377px;text-align:right;white-space:nowrap;font-size:19px;line-height:23px;font-weight:400;color:var(--olive-dark);}
  .hero-body{right:38px;text-align:right;white-space:nowrap;font-size:12.5px;line-height:16.6px;color:var(--olive-dark);}
  .hero-body.first{top:468px;}
  .hero-body.second{top:517px;}
  .section-tab{left:58px;top:667px;font-size:19px;font-weight:400;color:var(--white);letter-spacing:.2px;}
  .step-label{width:200px;text-align:center;font-size:16px;line-height:20px;color:var(--ink);}
  .step-label.one{left:41px;top:824px;}
  .step-label.two{left:321px;top:824px;}
  .step-label.three{left:598px;top:824px;}
  .why-heading{left:37px;top:908px;font-size:19px;font-weight:700;color:var(--olive);}
  .why-body{left:37px;top:934px;width:768px;font-size:12.9px;line-height:16.6px;text-align:justify;color:var(--ink);}
  .call-now{left:115px;top:1015px;font-size:22px;color:#444;}
  .phone{left:110px;top:1053px;font-size:16px;color:var(--ink);display:flex;align-items:center;gap:6px;}
  .web{left:438px;top:1057px;font-size:13px;letter-spacing:3px;color:var(--white);}
</style>
</head>
<body>
<article class="flyer">
  <svg class="flyer-shapes" viewBox="0 0 842 1090" xmlns="http://www.w3.org/2000/svg">
    <defs>
      <linearGradient id="crowdTone" x1="0" y1="0" x2="1" y2="1">
        <stop offset="0" stop-color="#2f3a52"/>
        <stop offset=".5" stop-color="#5a4a4a"/>
        <stop offset="1" stop-color="#2c2a30"/>
      </linearGradient>
    </defs>
    <rect class="hero-photo" x="0" y="0" width="842" height="662" fill="url(#crowdTone)" role="img" aria-label="Photo of Milo smiling with a microphone in front of a large conference audience"/>
    <polygon class="hero-corner" points="0,590 130,596 0,662" fill="#6a6a6a"/>
    <polygon class="hero-panel" points="842,222 842,660 130,598" fill="var(--lime)"/>
    <polygon class="page-body" points="0,662 130,597 842,660 842,1090 0,1090" fill="var(--white)"/>
    <polygon class="page-body-edge" points="130,597 842,660 842,662 130,599" fill="#e2e2e2"/>

    <polygon class="section-tab-shape" points="37,665 218,665 232,698 37,698" fill="var(--tab)"/>
    <line x1="230" y1="698" x2="805" y2="698" stroke="#8a8a8a" stroke-width="1.5"/>

    <polygon class="step-panel" points="37,702 240,702 277,798 240,895 37,895" fill="var(--panel)"/>
    <polygon class="step-panel" points="272,702 525,702 562,798 525,895 272,895 309,798" fill="var(--panel)"/>
    <polygon class="step-panel" points="557,702 805,702 805,895 557,895 594,798" fill="var(--panel)"/>

    <g class="step-badge" fill="var(--hex)" stroke="var(--white)" stroke-width="3">
      <polygon points="141,718 178,739 178,781 141,802 104,781 104,739"/>
      <polygon points="421,718 458,739 458,781 421,802 384,781 384,739"/>
      <polygon points="698,718 735,739 735,781 698,802 661,781 661,739"/>
    </g>
    <g font-family="Lato, sans-serif" font-size="42" fill="var(--white)" text-anchor="middle">
      <text x="141" y="776">1</text>
      <text x="421" y="776">2</text>
      <text x="698" y="776">3</text>
    </g>

    <rect class="footer-band" x="0" y="1047" width="842" height="43" fill="var(--footer)"/>
    <polygon class="phone-tag" points="92,1044 260,1044 252,1077 84,1077" fill="var(--lime)"/>
  </svg>

  <h2 class="abs hero-question">Did you know that 75%<br>of healthcare costs are<br>incurred by preventable diseases?</h2>
  <p class="abs hero-body first">Cardiovascular disease, cancer, and diabetes are the three<br>major causes of rising health care plans and are all preventable.</p>
  <p class="abs hero-body second">Milo and his team have spent decades learning how to increase productivity,<br>reduce absenteeism, and increase employee engagement, all leading to lowering<br>healthcare costs. Together, they have developed a system created to target the<br>masses all while addressing individual needs. Their corporate training challenges helps to<br>engrain positive habits through a carefully curated accountability and reward system.</p>

  <h3 class="abs section-tab">HOW IT WORKS:</h3>
  <p class="abs step-label one">evaluate the needs<br>of your business</p>
  <p class="abs step-label two">set up individualized<br>workshops based<br>on highest needs</p>
  <p class="abs step-label three">create a customized<br>corporate training<br>challenge.</p>

  <h3 class="abs why-heading">WHY MILO?</h3>
  <p class="abs why-body">Milo excels at motivational speaking. He is an author, a nutritionist and a professional athlete with a master’s degree in clinical nutrition. He is a teacher of corporate wellness at Fernhollow College and a health coach. Milo has been featured in national magazines, podcasts, and popular fitness websites. Milo’s own health issues put him on a quest to heal himself and others. With twenty-five years of experience and a passion for wellness, he can provide your company with an unforgettable experience.</p>

  <p class="abs call-now">CALL NOW</p>
  <p class="abs phone">
    <svg width="15" height="15" viewBox="0 0 24 24" aria-hidden="true"><path d="M6.6 10.8a15.1 15.1 0 0 0 6.6 6.6l2.2-2.2c.3-.3.7-.4 1-.2 1.1.4 2.3.6 3.6.6.6 0 1 .4 1 1V20c0 .6-.4 1-1 1A17 17 0 0 1 3 4c0-.6.4-1 1-1h3.5c.6 0 1 .4 1 1 0 1.3.2 2.5.6 3.6.1.3 0 .7-.2 1z" fill="#4b5a18"/></svg>
    (555)014-0192
  </p>
  <p class="abs web">www.milohartwell.com</p>
</article>
</body>
</html>
```